DL size flyer design for renovations and extensions construction company

We are looking for a flyer design for a construction company specialising in renovations, extensions, and minor building works. The aim is for anyone needing any home construction works to pick up the phone and call us. The flyers will be delivered primarily to letterboxes of homes. We want the flyers to stick out from all the other things people get in the mail by any means possible.

Target Market(s)

The audience we target is residential home owners and are looking to deliver these letters to home letterboxes.

Industry/Entity Type

Residential Construction

Font styles to use
Sans Serif

Colors
000000
ffffff

Requirements
Must have
• 1 - Places for 4 photos with descriptions reading: (1) Bathroom Renovations (4) Kitchen Renovations (3) Home Extensions (4) Outdoor works and landscaping. This may be on the reverse side of the DL flyer.
• 2 - Fonts to be used are (1) Brandon Grotesque (All caps) for main heading, (2) Montserrat SemiBold (All caps) for Headings, (3) Lato for text.
• 3 - Copy of the finished document in PDF and indesign formats.
• 4 - Placeholders for copy (look at the plinvaroq.com website for now)
Nice to have
• A modern looking design.
Should not have
• Not all photos attached are necessarily required. Up to you to use your creativity to decide on the best combination.

```html
<!DOCTYPE html>
<html lang="en">
<head>
<meta charset="utf-8">
<title>Services – Plinvaroq</title>
<link rel="stylesheet" href="https://fonts.googleapis.com/css2?family=Lato:wght@300;400&family=Montserrat:wght@600&display=swap">
<style>
:root{
  --ink:#000000;
  --paper:#ffffff;
  --accent:#22a06b;
  --text:#1a1a1a;
  --photo-bath-a:#d9d9d6;
  --photo-bath-b:#8d8e8c;
  --photo-kitchen-a:#eeeeec;
  --photo-kitchen-b:#b9b6b0;
  --photo-ext-a:#f2eee8;
  --photo-ext-b:#9a7350;
  --photo-garden-a:#6f9a3f;
  --photo-garden-b:#5a3a24;
}
*{margin:0;padding:0;box-sizing:border-box}
html,body{width:1200px;height:2542px;overflow:hidden;background:var(--paper)}
.flyer{position:relative;width:1200px;height:2542px;background:var(--paper);font-family:"Lato",sans-serif;color:var(--text)}
.header{position:absolute;left:0;top:0;width:1200px;height:216px}
.header svg{position:absolute;inset:0}
.header-title{position:absolute;left:360px;right:0;top:40px;text-align:center;font-family:"Lato",sans-serif;font-weight:400;font-size:104px;letter-spacing:4px;color:var(--paper);line-height:1.1}
.service-heading{position:absolute;height:173px;background:var(--ink);color:var(--paper);font-family:"Montserrat",sans-serif;font-weight:600;font-size:50px;line-height:1.12;display:flex;align-items:center;overflow:hidden}
.service-heading svg{position:absolute;inset:0}
.service-heading span{position:relative}
.heading-left{left:0;width:681px;justify-content:flex-end;padding-right:70px;text-align:right}
.heading-right{left:519px;width:681px;justify-content:flex-start;padding-left:56px}
.heading-compact{font-size:44px;line-height:1.06;height:170px}
.photo{position:absolute}
.photo-bathroom{left:702px;top:247px;width:498px;height:465px;background:linear-gradient(135deg,var(--photo-bath-a),var(--photo-bath-b))}
.photo-kitchen{left:0;top:813px;width:498px;height:470px;background:linear-gradient(160deg,var(--photo-kitchen-a),var(--photo-kitchen-b))}
.photo-extension{left:702px;top:1327px;width:498px;height:465px;background:linear-gradient(150deg,var(--photo-ext-a),var(--photo-ext-b))}
.photo-garden{left:0;top:1863px;width:498px;height:475px;background:linear-gradient(170deg,var(--photo-garden-a),var(--photo-garden-b))}
.copy{position:absolute;font-size:29px;line-height:1.16;text-align:justify}
.copy p+p{margin-top:18px}
.copy-bathroom{left:56px;top:427px;width:1090px}
.copy-bathroom .wrap-space{float:right;width:465px;height:290px}
.copy-kitchen{left:521px;top:1000px;width:625px}
.copy-extension{left:56px;top:1507px;width:625px}
.copy-garden{left:521px;top:2040px;width:625px}
.footer{position:absolute;left:0;top:2380px;width:1200px;height:162px}
.footer svg{position:absolute;inset:0}
.footer-url{position:absolute;left:0;right:0;bottom:28px;text-align:center;font-family:"Lato",sans-serif;font-size:56px;color:var(--paper);letter-spacing:1px}
</style>
</head>
<body>
<main class="flyer">

  <header class="header">
    <svg width="1200" height="216" viewBox="0 0 1200 216" aria-hidden="true">
      <rect width="1200" height="216" fill="var(--ink)"/>
      <polygon points="0,0 330,0 420,216 0,216" fill="var(--paper)"/>
      <polygon points="0,0 300,0 390,216 0,216" fill="var(--accent)"/>
    </svg>
    <h1 class="header-title">SERVICES</h1>
  </header>

  <section class="service">
    <h2 class="service-heading heading-left" style="top:247px">
      <svg width="681" height="173" viewBox="0 0 681 173" aria-hidden="true"><polygon points="0,0 150,0 0,120" fill="var(--accent)"/></svg>
      <span>Bathroom<br>Renovations</span>
    </h2>
    <div class="photo photo-bathroom" role="img" aria-label="Bright modern bathroom with freestanding bath and glass shower"></div>
    <div class="copy copy-bathroom">
      <div class="wrap-space"></div>
      <p>We create custom bathroom renovations of various shapes and sizes to suit a variety of family needs.</p>
      <p>When considering a bathroom design you will need to take into account a variety of factors including the size of the existing space and whether it can be enlarged, how many people in your family will use the bathroom, if your family size is likely to increase, where the bathroom is located in the home as well as many other considerations.</p>
    </div>
  </section>

  <section class="service">
    <div class="photo photo-kitchen" role="img" aria-label="Light grey modern kitchen with stainless steel appliances"></div>
    <h2 class="service-heading heading-right" style="top:813px">
      <svg width="681" height="178" viewBox="0 0 681 178" aria-hidden="true"><polygon points="681,20 681,178 500,178" fill="var(--accent)"/></svg>
      <span>Kitchen<br>Renovations</span>
    </h2>
    <div class="copy copy-kitchen">
      <p>Today's kitchens go further than places to just make a meal - they are the open-plan hub for the modern home.</p>
      <p>Each kitchen will need to work in with each family's unique needs. That's why it's important to work in with an expert designer and builder on your renovation project.</p>
    </div>
  </section>

  <section class="service">
    <h2 class="service-heading heading-left" style="top:1327px">
      <svg width="681" height="173" viewBox="0 0 681 173" aria-hidden="true"><polygon points="0,0 150,0 0,120" fill="var(--accent)"/></svg>
      <span>Home<br>Extensions</span>
    </h2>
    <div class="photo photo-extension" role="img" aria-label="Open-plan extension with timber dining table and pendant lights"></div>
    <div class="copy copy-extension">
      <p>Structural alterations or extensions are an essential consideration when things simply wont fit or you want to make your home bigger or better.</p>
      <p>Plinvaroq are licenced builders experienced at delivering structural alterations or home extensions, and we are always guided by our qualified engineers.</p>
    </div>
  </section>

  <section class="service">
    <div class="photo photo-garden" role="img" aria-label="Landscaped garden with timber bench and planted beds"></div>
    <h2 class="service-heading heading-right heading-compact" style="top:1863px">
      <svg width="681" height="170" viewBox="0 0 681 170" aria-hidden="true"><polygon points="681,20 681,170 500,170" fill="var(--accent)"/></svg>
      <span>Outdoor works and<br>landscaping<br>Renovations</span>
    </h2>
    <div class="copy copy-garden">
      <p>Home living spans across both internal and external environments and a complete home needs to consider integration into the surrounding land.</p>
      <p>Whether it be landscaping works, swimming pools or outdoor buildings - Plinvaroq can deliver all project designs both large scale and compact.</p>
    </div>
  </section>

  <footer class="footer">
    <svg width="1200" height="162" viewBox="0 0 1200 162" aria-hidden="true">
      <polygon points="0,40 1200,40 1200,162 0,162" fill="var(--ink)"/>
      <polygon points="0,0 90,0 180,162 0,162" fill="var(--accent)"/>
      <polygon points="0,40 70,40 0,130" fill="var(--accent)"/>
    </svg>
    <p class="footer-url">www.plinvaroq.com</p>
  </footer>

</main>
</body>
</html>
```